Corvane Gulfside LLC

we need a business card design

Industry/Entity Type

hvac

Contact Information for Business Card

my logo

Requirements
Must have
• my logo and same colors

```html
<!DOCTYPE html>
<html lang="en">
<head>
<meta charset="utf-8">
<title>Corvane Gulfside LLC – Business Card</title>
<link href="https://fonts.googleapis.com/css2?family=Inter:wght@400;500;600;700&display=swap" rel="stylesheet">
<style>
  :root {
    --page-bg: #e0e0e0;
    --card-dark: #444444;
    --card-light: #ffffff;
    --brand-blue: #1b5ba6;
    --brand-orange: #f9b54a;
    --brand-sky: #37b8d8;
    --text-grey: #555555;
    --strip: linear-gradient(90deg, #2f5fa0 0%, #8e8a94 30%, #f9b54a 52%, #c9c48e 72%, #37b8d8 100%);
  }
  * { margin: 0; padding: 0; box-sizing: border-box; }
  html, body { width: 1200px; height: 1200px; overflow: hidden; }
  body {
    background: var(--page-bg);
    font-family: "Inter", Arial, sans-serif;
    position: relative;
  }
  .card {
    position: absolute;
    left: 179px;
    width: 861px;
    height: 495px;
    overflow: hidden;
    box-shadow: 0 12px 22px rgba(0,0,0,0.28);
  }
  .card::after {
    content: "";
    position: absolute;
    left: 0; right: 0; bottom: 0;
    height: 15px;
    background: var(--strip);
  }
  .card--front { top: 84px; background: var(--card-dark); }
  .card--back { top: 621px; background: var(--card-light); }

  .brand-mark {
    position: absolute;
    display: flex;
    align-items: center;
    gap: 14px;
    transform: translate(-50%, -50%);
    white-space: nowrap;
  }
  .brand-mark__dot {
    width: 22px; height: 22px;
    border-radius: 50%;
    background: var(--brand-orange);
    flex: none;
  }
  .brand-mark__name {
    font-weight: 700;
    letter-spacing: 0.5px;
  }
  .card--front .brand-mark { left: 430px; top: 251px; }
  .card--front .brand-mark__name { color: #ffffff; font-size: 40px; }
  .card--back .brand-mark { left: 622px; top: 230px; }
  .card--back .brand-mark__name { color: var(--brand-blue); font-size: 28px; }

  .person { position: absolute; left: 49px; top: 62px; }
  .person__name {
    color: var(--brand-blue);
    font-weight: 700;
    font-size: 31px;
    letter-spacing: 1.5px;
    line-height: 1;
  }
  .person__role {
    color: var(--text-grey);
    font-size: 27px;
    font-weight: 400;
    letter-spacing: 1.2px;
    margin-top: 10px;
    margin-left: -4px;
    line-height: 1;
  }
  .person__rule {
    width: 137px; height: 3px;
    background: var(--brand-orange);
    margin-top: 12px;
  }
  .address {
    position: absolute;
    left: 47px; top: 196px;
    color: var(--text-grey);
    font-size: 26px;
    font-weight: 500;
    letter-spacing: 4.3px;
    line-height: 36px;
  }
  .contact {
    position: absolute;
    left: 40px; top: 328px;
    list-style: none;
  }
  .contact__item {
    display: flex;
    align-items: center;
    gap: 16px;
    height: 39px;
    color: var(--text-grey);
    font-size: 26px;
    font-weight: 500;
    letter-spacing: 4.3px;
  }
  .contact__icon { width: 26px; height: 26px; flex: none; fill: var(--brand-blue); }
</style>
</head>
<body>

  <section class="card card--front">
    <div class="brand-mark">
      <span class="brand-mark__dot"></span>
      <span class="brand-mark__name">Corvane Gulfside LLC</span>
    </div>
  </section>

  <section class="card card--back">
    <div class="person">
      <h1 class="person__name">JONATHAN SMITH</h1>
      <p class="person__role">DIRECTOR</p>
      <div class="person__rule"></div>
    </div>

    <p class="address">Anywhere St.<br>Any City, ST 123</p>

    <ul class="contact">
      <li class="contact__item">
        <svg class="contact__icon" viewBox="0 0 24 24" aria-hidden="true">
          <path d="M6.6 10.8a15.1 15.1 0 0 0 6.6 6.6l2.2-2.2c.3-.3.7-.4 1-.2 1.1.4 2.3.6 3.6.6.6 0 1 .4 1 1V20c0 .6-.4 1-1 1C10.6 21 3 13.4 3 4c0-.6.4-1 1-1h3.5c.6 0 1 .4 1 1 0 1.3.2 2.5.6 3.6.1.3 0 .7-.2 1z"/>
        </svg>
        <span>800-222-2222</span>
      </li>
      <li class="contact__item">
        <svg class="contact__icon" viewBox="0 0 24 24" aria-hidden="true">
          <path d="M2 6h20v13H2z M2 6l10 7 10-7" fill="none" stroke="#1b5ba6" stroke-width="2"/>
          <path d="M2 6h20l-10 7z"/>
        </svg>
        <span>email@yoursite.com</span>
      </li>
      <li class="contact__item">
        <svg class="contact__icon" viewBox="0 0 24 24" aria-hidden="true">
          <g fill="none" stroke="#1b5ba6" stroke-width="1.8">
            <circle cx="12" cy="12" r="9.5"/>
            <ellipse cx="12" cy="12" rx="4.2" ry="9.5"/>
            <path d="M2.5 12h19M4 7h16M4 17h16M12 2.5v19"/>
          </g>
        </svg>
        <span>www.yoursite.com</span>
      </li>
    </ul>

    <div class="brand-mark">
      <span class="brand-mark__dot"></span>
      <span class="brand-mark__name">Corvane Gulfside LLC</span>
    </div>
  </section>

</body>
</html>
```